Online Certificate in Research Methods needs a Digital Banner ad

We are launching an online graduate certificate in Quantitative and Qualitative Social Science Research Methods. We need a digital banner created so we can advertise on plimora, zentrik, and some other places.

The banner needs to use these color schemes and fonts: https://universityrelations.marlowecrest.edu/brand-guide/color

Would like the banner to say (either as three lines, or if not in three lines, have these sets of words at minimum on the same line):
Online Graduate Certificate in
Quantitative & Qualitative
Social Science Research Methods

We also want it to say Marlowe Crest University and Next Start Date August 18, 2021. I’ve attached a picture of a version we tried to create but is hard to read.

We need a graphic that looks good in the following specs:
600px wide x 70px tall, high quality (at least 300 dpi) jpg or png

And
Plimora recommendations:
Design Recommendations
• File Type: JPG or PNG
• Ratio: 1.91:1 to 1:1
• Resolution: At least 1080 x 1080 pixels
Text Recommendations
• Primary Text: 125 characters
• Headline: 40 characters
• Description: 30 characters
Technical Requirements
• Maximum File Size: 30MB
• Minimum Width: 600 pixels
• Minimum Height: 600 pixels
• Aspect Ratio Tolerance: 3%

```html
<!DOCTYPE html>
<html lang="en">
<head>
<meta charset="utf-8">
<title>Research Methods Certificate – Digital Banners</title>
<link rel="stylesheet" href="https://fonts.googleapis.com/css2?family=Roboto+Condensed:ital,wght@0,700;1,700&family=Roboto:wght@700&display=swap">
<style>
  :root {
    --navy: #002855;
    --navy-deep: #001b3d;
    --navy-soft: #0b3566;
    --gold: #eaaa00;
    --gold-light: #f6c433;
    --gold-deep: #c98f00;
    --white: #ffffff;
    --ink: #111111;
    --photo-light: #e9e6e1;
    --photo-mid: #b9a89a;
    --photo-dark: #6d5a52;
  }
  * { box-sizing: border-box; margin: 0; padding: 0; }
  html, body {
    width: 1200px; height: 1000px; overflow: hidden;
    background: var(--white);
    font-family: "Roboto Condensed", "Arial Narrow", sans-serif;
  }
  .size-label {
    position: absolute; left: 0; width: 1200px; text-align: center;
    font-family: "Roboto Condensed", sans-serif; font-weight: 700;
    font-size: 33px; line-height: 36px; color: var(--ink); letter-spacing: 0.2px;
  }
  .size-label--square { top: 34px; }
  .size-label--leader { top: 930px; }

  /* Square ad */
  .ad-square {
    position: absolute; left: 280px; top: 94px; width: 640px; height: 640px;
    overflow: hidden;
  }
  .ad-square__bg { position: absolute; inset: 0; }
  .brand-name {
    position: absolute; display: flex; align-items: center; gap: 8px;
    font-family: "Roboto Condensed", sans-serif; font-weight: 700;
    color: var(--navy); white-space: nowrap;
  }
  .brand-name__mark { background: var(--gold); flex: none; }
  .ad-square .brand-name { right: 24px; top: 44px; font-size: 27px; }
  .ad-square .brand-name__mark { width: 22px; height: 22px; }

  .headline {
    position: absolute; color: var(--white); font-weight: 700;
    text-transform: uppercase; white-space: nowrap;
  }
  .ad-square .headline { left: 48px; top: 347px; font-size: 35px; line-height: 34px; }
  .start-date {
    position: absolute; color: var(--gold); font-weight: 700; font-style: italic;
    text-transform: uppercase; white-space: nowrap;
  }
  .ad-square .start-date { left: 49px; top: 459px; font-size: 24.5px; line-height: 28px; }

  .cta {
    position: absolute; display: flex; align-items: center;
    border-radius: 40px; text-decoration: none;
    font-family: "Roboto", Arial, sans-serif; font-weight: 700; white-space: nowrap;
  }
  .cta__text { display: flex; flex-direction: column; line-height: 1; }
  .cta--gold {
    left: 47px; top: 524px; width: 233px; height: 74px;
    background: linear-gradient(180deg, var(--gold-light) 0%, var(--gold) 55%, var(--gold-deep) 100%);
    box-shadow: 0 0 0 3px rgba(0,0,0,0.18), 0 6px 14px rgba(0,0,0,0.45);
    color: var(--navy); padding-left: 40px; gap: 12px;
  }
  .cta--gold .cta__small { font-size: 17px; margin-bottom: 2px; padding-left: 1px; }
  .cta--gold .cta__big { font-size: 27px; }

  /* Leaderboard ad */
  .ad-leader {
    position: absolute; left: 45px; top: 776px; width: 1110px; height: 130px;
    overflow: hidden;
  }
  .ad-leader__bg { position: absolute; inset: 0; }
  .ad-leader .headline {
    left: 90px; width: 440px; top: 17px; text-align: center;
    font-size: 23px; line-height: 24px;
  }
  .ad-leader .start-date { left: 90px; width: 440px; top: 93px; text-align: center; font-size: 18.5px; line-height: 22px; }
  .cta--navy {
    left: 886px; top: 16px; width: 180px; height: 58px;
    background: linear-gradient(180deg, var(--navy-soft) 0%, var(--navy) 60%, var(--navy-deep) 100%);
    box-shadow: 0 0 0 3px rgba(0,0,0,0.2), 0 4px 10px rgba(0,0,0,0.35);
    color: var(--white); padding-left: 30px; gap: 8px;
  }
  .cta--navy .cta__small { font-size: 13px; margin-bottom: 1px; }
  .cta--navy .cta__big { font-size: 20.5px; }
  .ad-leader .brand-name { left: 898px; top: 94px; font-size: 15px; gap: 5px; }
  .ad-leader .brand-name__mark { width: 12px; height: 12px; }
</style>
</head>
<body>

<div class="size-label size-label--square">1080x1080 pixels</div>

<section class="ad-square" aria-label="Square social ad">
  <svg class="ad-square__bg" width="640" height="640" viewBox="0 0 640 640">
    <defs>
      <linearGradient id="sq-photo" x1="0" y1="0" x2="1" y2="0.4">
        <stop offset="0" stop-color="var(--photo-dark)"/>
        <stop offset="0.35" stop-color="var(--photo-mid)"/>
        <stop offset="0.75" stop-color="var(--photo-light)"/>
        <stop offset="1" stop-color="#f7f6f4"/>
      </linearGradient>
      <linearGradient id="sq-navy" x1="0" y1="0" x2="0" y2="1">
        <stop offset="0" stop-color="var(--navy-deep)"/>
        <stop offset="1" stop-color="var(--navy)"/>
      </linearGradient>
    </defs>
    <rect width="640" height="300" fill="url(#sq-photo)" role="img" aria-label="Photo of students working on laptops in a classroom"/>
    <path d="M0,228 Q60,306 200,294 L640,182 V640 H0 Z" fill="var(--gold)"/>
    <path d="M0,250 Q60,314 205,302 L640,198 V640 H0 Z" fill="url(#sq-navy)"/>
  </svg>

  <div class="brand-name"><span class="brand-name__mark"></span>Marlowe Crest University</div>

  <h1 class="headline">Online Graduate Certificate in<br>Quantitative &amp; Qualitative<br>Social Science Research Methods</h1>
  <p class="start-date">Next Start Date August 18, 2021</p>

  <a class="cta cta--gold" href="#">
    <svg width="26" height="30" viewBox="0 0 26 30" aria-hidden="true">
      <path d="M2,2 L12,15 L2,28 M13,2 L23,15 L13,28" fill="none" stroke="var(--navy)" stroke-width="5" stroke-linejoin="miter"/>
    </svg>
    <span class="cta__text"><span class="cta__small">Click here for</span><span class="cta__big">More Info</span></span>
  </a>
</section>

<section class="ad-leader" aria-label="Leaderboard banner ad">
  <svg class="ad-leader__bg" width="1110" height="130" viewBox="0 0 1110 130">
    <defs>
      <linearGradient id="ld-photo" x1="0" y1="0" x2="1" y2="0">
        <stop offset="0" stop-color="var(--photo-dark)"/>
        <stop offset="0.4" stop-color="var(--photo-mid)"/>
        <stop offset="1" stop-color="var(--photo-light)"/>
      </linearGradient>
      <linearGradient id="ld-gold" x1="0" y1="0" x2="1" y2="0">
        <stop offset="0" stop-color="var(--gold)" stop-opacity="0"/>
        <stop offset="0.25" stop-color="var(--gold)"/>
        <stop offset="1" stop-color="var(--gold-light)"/>
      </linearGradient>
      <radialGradient id="ld-glow" cx="0.55" cy="0.85" r="0.6">
        <stop offset="0" stop-color="#fff4cf"/>
        <stop offset="1" stop-color="#fff4cf" stop-opacity="0"/>
      </radialGradient>
    </defs>
    <rect width="1110" height="130" fill="var(--navy)"/>
    <path d="M0,58 L56,130 H76 L0,32 Z" fill="var(--gold)"/>
    <path d="M548,130 L582,0 H880 V130 Z" fill="url(#ld-photo)" role="img" aria-label="Photo of students working on laptops in a classroom"/>
    <rect x="780" y="0" width="330" height="130" fill="url(#ld-gold)"/>
    <rect x="780" y="0" width="330" height="130" fill="url(#ld-glow)"/>
  </svg>

  <h2 class="headline">Online Graduate Certificate in<br>Quantitative &amp; Qualitative<br>Social Science Research Methods</h2>
  <p class="start-date">Next Start Date August 18, 2021</p>

  <a class="cta cta--navy" href="#">
    <svg width="20" height="24" viewBox="0 0 20 24" aria-hidden="true">
      <path d="M2,2 L9,12 L2,22 M10,2 L17,12 L10,22" fill="none" stroke="var(--white)" stroke-width="4"/>
    </svg>
    <span class="cta__text"><span class="cta__small">Click here for</span><span class="cta__big">More Info</span></span>
  </a>

  <div class="brand-name"><span class="brand-name__mark"></span>Marlowe Crest University</div>
</section>

<div class="size-label size-label--leader">600x70 pixels</div>

</body>
</html>
```